Take an existing presentation and make it more dynamic and professional.

We have an existing powerpoint presentation that we are using both as a presentation tool and also with a voice over on Youtube.

Content is pretty much there. Needs a new theme that is modern and contemporary.

Can answer questions regarding all slides as we have added a few new ones in just for this project.

Can also provide links to the youtube vid so you understand what voice over depicts in regards to the presentation

More relevant graphics may need to be use to create a uniform feel throughout the presentation.

We are looking for an awesome designer who really knows power point to create something truly spectacular. In most cases this will be the first presentation that someone sees of our company so it must be exactly right.

You can watch the Youtube video here. http://vidlume.example/Qx7RtmW2kBp

Target Market(s)

People seeking to start a business. We are offering an opportunity to partner with us in a lucrative business model which has low start up costs but very quick financial rewards over the first 3 months. The products are back by 25 years of scientific research and 100% of the people that use them they work on.

Industry/Entity Type

It Company

Font styles to use
Sans Serif

Colors
0492cd
33a6d7
85cae6
cee9f5
ebf7f9
0255a3

Requirements
Must have
• Modern professional clean look. Good transitions, Relevant images.
• First slide title, logo and background to stay unless you come up with a better background.
• Colors should be blues.
• Slide with the bottles should have new better looking graphics. All 8 bottles should be pointing to s single bottle in the centre. A theme that we can apply to our other presentations. Though if the project turns out the way we hope we will provide the contest winner with our other presentations to fix.
Nice to have
• Some slides can be combined.
Should not have
• Images that do not fit with the theme, anything that distracts from the message of the slides both text and images should be complementary.

```html
<!DOCTYPE html>
<html lang="en">
<head>
<meta charset="utf-8">
<title>Nodewell Labs – Presentation Theme</title>
<link rel="stylesheet" href="https://fonts.googleapis.com/css2?family=PT+Sans+Narrow:wght@400;700&family=PT+Sans:ital,wght@1,400&display=swap">
<style>
  :root{
    --stage:#1f2427;
    --navy-text:#173f78;
    --brand-blue:#0492cd;
    --ring-blue:#1a6cc0;
    --band-top:#3a78c0;
    --band-bottom:#164b8d;
    --button-top:#1f4f8c;
    --button-bottom:#0f3668;
    --slide-white:#f6f7f8;
    --slide-grey:#e9ecee;
    --hero-dark:#3c3c3c;
    --hero-mid:#6e6e6e;
    --body-text:#1f2a36;
    --tick:#1e5fa8;
  }
  *{box-sizing:border-box;margin:0;padding:0}
  html,body{width:1200px;height:1000px;overflow:hidden;background:var(--stage)}
  body{position:relative;font-family:"PT Sans Narrow",sans-serif}

  .slide{position:absolute;width:587px;height:442px;overflow:hidden;
    background:linear-gradient(135deg,var(--slide-white) 0%,#ffffff 45%,var(--slide-grey) 100%);
    box-shadow:0 2px 8px rgba(0,0,0,.6)}
  .slide--cover{left:8px;top:54px}
  .slide--blank{left:605px;top:54px}
  .slide--company{left:8px;top:505px}
  .slide--network{left:605px;top:505px}

  /* footer band */
  .footer-band{position:absolute;left:0;right:0;bottom:0;height:44px;
    background:linear-gradient(var(--band-top),var(--band-bottom));
    border-top:2px solid #5d95d3}
  .footer-text{position:absolute;left:20px;top:12px;color:#fff;
    font-family:"PT Sans",sans-serif;font-style:italic;font-size:13px}
  .nav-button{position:absolute;top:8px;height:27px;width:48px;border-radius:5px;
    background:linear-gradient(var(--button-top),var(--button-bottom));
    color:#fff;font-family:Arial,sans-serif;font-size:12px;line-height:27px;text-align:center;
    box-shadow:inset 0 1px 0 rgba(255,255,255,.25)}
  .nav-button--back{left:468px}
  .nav-button--next{left:525px}

  /* brand wordmark stand-in */
  .brand{position:absolute;display:flex;align-items:center;gap:8px}
  .brand-dot{width:26px;height:26px;border-radius:50%;background:var(--brand-blue)}
  .brand-name{font-family:"PT Sans Narrow",sans-serif;font-weight:400;font-size:24px;color:var(--brand-blue);line-height:1}

  /* cover slide */
  .hero-band{position:absolute;left:0;top:0;width:100%;height:258px;
    background:linear-gradient(180deg,var(--hero-mid) 0%,var(--hero-dark) 100%)}
  .hero-rule{position:absolute;left:0;top:258px;width:100%;height:6px;background:var(--ring-blue)}
  .portrait-ring{position:absolute;left:18px;top:152px;width:214px;height:214px;border-radius:50%;
    background:var(--ring-blue);padding:8px}
  .portrait{width:100%;height:100%;border-radius:50%;border:4px solid #fff;
    background:radial-gradient(circle at 50% 45%,#cfc6bf 0%,#8d8580 55%,#3a3d44 100%)}
  .cover-title{position:absolute;right:34px;top:96px;color:#fff;font-weight:700;font-size:34px;
    text-shadow:0 1px 2px rgba(0,0,0,.4)}
  .cover-subtext{position:absolute;right:34px;top:142px;width:360px;text-align:right;color:#eee;
    font-size:14px;line-height:20px}
  .cover-date{left:53px}

  /* content slides */
  .title-flag{position:absolute;left:0;top:12px;width:22px;height:31px}
  .slide-title{position:absolute;left:28px;top:10px;font-weight:700;font-size:27px;color:var(--navy-text)}
  .section-heading{position:absolute;left:43px;top:71px;font-weight:700;font-size:18px;color:var(--navy-text)}
  .tick-list{position:absolute;left:43px;top:101px;list-style:none;font-size:13px;line-height:19.1px;color:var(--body-text)}
  .tick-list li{position:relative;padding-left:23px}
  .tick-list li::before{content:"";position:absolute;left:3px;top:2px;width:6px;height:12px;
    border:solid var(--tick);border-width:0 4px 4px 0;transform:rotate(40deg)}
  .tick-list--company{width:460px}
  .team-photo{position:absolute;left:213px;top:95px;width:345px;height:280px;
    background:linear-gradient(180deg,#d8dbe0 0%,#8f939b 45%,#f1f2f4 100%);border-radius:4px}
</style>
</head>
<body>

<section class="slide slide--cover">
  <div class="hero-band"></div>
  <div class="hero-rule"></div>
  <h1 class="cover-title">Project Title Here</h1>
  <p class="cover-subtext">Subtext here Subtext here Subtext here Subtext here<br>Subtext here Subtext here Subtext here</p>
  <div class="portrait-ring"><div class="portrait" role="img" aria-label="Portrait photo of the presenter"></div></div>
  <div class="brand" style="left:376px;top:318px"><span class="brand-dot"></span><span class="brand-name">Nodewell Labs</span></div>
  <footer class="footer-band">
    <span class="footer-text cover-date">Saturday, 31 January 2015</span>
    <span class="nav-button nav-button--next">Start</span>
  </footer>
</section>

<section class="slide slide--blank">
  <svg class="title-flag" viewBox="0 0 22 31"><polygon points="0,0 22,0 22,31 0,31 9,15.5" fill="var(--ring-blue)"/></svg>
  <h2 class="slide-title">Slide Title Presentation</h2>
  <div class="brand" style="left:413px;top:343px"><span class="brand-dot"></span><span class="brand-name">Nodewell Labs</span></div>
  <footer class="footer-band">
    <span class="footer-text">Timeline about your Slide Presentation</span>
    <span class="nav-button nav-button--back">Back</span>
    <span class="nav-button nav-button--next">Next</span>
  </footer>
</section>

<section class="slide slide--company">
  <svg class="title-flag" viewBox="0 0 22 31"><polygon points="0,0 22,0 22,31 0,31 9,15.5" fill="var(--ring-blue)"/></svg>
  <h2 class="slide-title">Slide Title Presentation</h2>
  <h3 class="section-heading">Cove Modern Realty</h3>
  <ul class="tick-list tick-list--company">
    <li>High volume local boutique real estate company</li>
    <li>Specialize in selling homes throughout the San Francisco Bay Area</li>
    <li>Focus on modern marketing techniques and thinking outside the box</li>
    <li>“High Tech and High Touch” approach to real estate</li>
    <li>Certified Green Business Everything is done and stored online. No File Cabinets in our offices!</li>
    <li>Exceptional web presence far beyond other local real estate companies</li>
    <li>Clean, streamline, and hip marketing materials</li>
    <li>A company constantly looking into the latest real estate trends, tools, and technology to better assist their agents and clients sell homes in the modern world, all while embracing tried and true real estate values and practices as well</li>
    <li>Leading authority for architectural homes and recognized world wide</li>
    <li>Not Just Modern Homes! We focus on Modern Real Estate<br>Practices through and through.</li>
  </ul>
  <div class="brand" style="left:413px;top:343px"><span class="brand-dot"></span><span class="brand-name">Nodewell Labs</span></div>
  <footer class="footer-band">
    <span class="footer-text">Timeline about your Slide Presentation</span>
    <span class="nav-button nav-button--back">Back</span>
    <span class="nav-button nav-button--next">Next</span>
  </footer>
</section>

<section class="slide slide--network">
  <svg class="title-flag" viewBox="0 0 22 31"><polygon points="0,0 22,0 22,31 0,31 9,15.5" fill="var(--ring-blue)"/></svg>
  <h2 class="slide-title">Slide Title Presentation</h2>
  <h3 class="section-heading">I’ve got connections!</h3>
  <ul class="tick-list">
    <li>Handymen</li>
    <li>Contractors</li>
    <li>Stagers</li>
    <li>Painters</li>
    <li>Cleaners</li>
    <li>Movers</li>
    <li>Storage companies</li>
    <li>Landscapers</li>
    <li>Estate Sale Professionals</li>
    <li>Lawyers</li>
    <li>Mortgage Brokers</li>
    <li>Inspectors</li>
  </ul>
  <div class="team-photo" role="img" aria-label="Group photo of business professionals and tradespeople standing together"></div>
  <div class="brand" style="left:413px;top:343px"><span class="brand-dot"></span><span class="brand-name">Nodewell Labs</span></div>
  <footer class="footer-band">
    <span class="footer-text">Timeline about your Slide Presentation</span>
    <span class="nav-button nav-button--back">Back</span>
    <span class="nav-button nav-button--next">Next</span>
  </footer>
</section>

</body>
</html>
```